Visual consulting framework

Thornwell Advisory is a financial consulting business that takes it clients on the following journey:
1. Get fit (disciplined)
2. Get funded (access to capital)
3. Get big (grow)
4. Get out (exit with wealth)
Over thirty years we have identified that the key to being successful on this journey are the following elements or components.
1. Vision
2. Strategy
3. Structure
4. Product & services
5. Sales and marketing
6. System and processes
7. People
8. Culture
9. Finance
10. M&A
11. Performance monitoring
12. Risk management
We require a visual representation of these elements and the journey to communicate to clients and prospects in marketing material.
Look and feel
Each slider illustrates characteristics of the customer's brand and the style your logo design should communicate.

```html
<!DOCTYPE html>
<html lang="en">
<head>
<meta charset="utf-8">
<title>Thornwell Advisory – Consulting Framework</title>
<link rel="stylesheet" href="https://fonts.googleapis.com/css2?family=Bebas+Neue&family=Raleway:wght@500&display=swap">
<style>
  :root {
    --blue: #00a8ea;
    --orange: #f68e21;
    --white: #ffffff;
    --backdrop: #ececec;
  }
  html, body {
    margin: 0;
    padding: 0;
    width: 800px;
    height: 1200px;
    overflow: hidden;
    background: var(--backdrop);
  }
  .canvas {
    position: relative;
    width: 800px;
    height: 1200px;
  }
  .card {
    position: absolute;
    left: 0;
    top: 0;
    width: 1224px;
    height: 945px;
    background: var(--white);
    transform-origin: 0 0;
    transform: translate(20px, 307px) scale(0.6209);
    overflow: hidden;
    box-shadow: 0 4px 18px rgba(0,0,0,0.12);
  }
  .header-band {
    position: absolute;
    left: 0; top: 0;
    width: 1224px; height: 160px;
    background: var(--blue);
  }
  .headline {
    position: absolute;
    left: 77px; top: 36px;
    width: 700px;
    margin: 0;
    font-family: "Bebas Neue", sans-serif;
    font-weight: 400;
    font-size: 46px;
    line-height: 48px;
    color: var(--white);
    letter-spacing: 0;
    white-space: nowrap;
    z-index: 1;
  }
  .brand-tab {
    position: absolute;
    left: 793px; top: 0;
    width: 520px; height: 162px;
    background: var(--white);
    border-radius: 81px 0 0 81px;
    box-shadow: 0 4px 10px rgba(0,0,0,0.18);
    display: flex;
    align-items: center;
    padding-left: 80px;
    box-sizing: border-box;
    gap: 16px;
    z-index: 2;
  }
  .brand-dot {
    width: 34px; height: 34px;
    border-radius: 50%;
    background: var(--orange);
    flex: none;
  }
  .brand-name {
    font-family: "Raleway", sans-serif;
    font-weight: 500;
    font-size: 30px;
    line-height: 34px;
    color: var(--blue);
    text-transform: uppercase;
    letter-spacing: 1px;
  }
  .stage-spine {
    position: absolute;
    left: 152px; top: 317px;
    width: 2px; height: 498px;
    background: var(--blue);
  }
  .stage {
    position: absolute;
    left: 78px;
    width: 150px; height: 150px;
    box-sizing: border-box;
    border: 2px solid var(--blue);
    border-radius: 50%;
    background: var(--white);
    display: flex;
    align-items: center;
    justify-content: center;
  }
  .stage-core {
    width: 116px; height: 116px;
    border-radius: 50%;
    background: var(--blue);
    color: var(--white);
    font-family: "Bebas Neue", sans-serif;
    font-size: 36px;
    line-height: 31px;
    text-align: center;
    display: flex;
    align-items: center;
    justify-content: center;
    box-shadow: 0 3px 6px rgba(0,0,0,0.2);
  }
  .stage-link {
    position: absolute;
    left: 228px;
    width: 38px; height: 2px;
    background: var(--blue);
  }
  .stage-link::after {
    content: "";
    position: absolute;
    right: -4px; top: -4px;
    width: 6px; height: 6px;
    border: 2px solid var(--blue);
    border-radius: 50%;
    background: var(--white);
  }
  .goal {
    position: absolute;
    left: 265px;
    width: 893px; height: 50px;
    box-sizing: border-box;
    border: 3px solid var(--blue);
    border-radius: 25px;
    color: var(--blue);
    font-family: "Bebas Neue", sans-serif;
    font-size: 34px;
    line-height: 46px;
    text-align: center;
  }
  .element-row {
    position: absolute;
    left: 265px;
    width: 893px; height: 51px;
  }
  .element-row::before {
    content: "";
    position: absolute;
    left: 20px; right: 20px; top: 24px;
    height: 2px;
    background: var(--orange);
  }
  .element {
    position: absolute;
    top: 0;
    width: 284px; height: 51px;
    border-radius: 25px;
    background: var(--orange);
    color: var(--white);
    font-family: "Raleway", sans-serif;
    font-weight: 500;
    font-size: 19px;
    line-height: 18px;
    text-transform: uppercase;
    text-align: center;
    display: flex;
    align-items: center;
    justify-content: center;
  }
  .element:nth-child(1) { left: 0; }
  .element:nth-child(2) { left: 304px; }
  .element:nth-child(3) { left: 609px; }
  .footer-bar {
    position: absolute;
    left: 0; bottom: 0;
    width: 1224px; height: 15px;
    background: linear-gradient(to right, var(--orange) 0 611px, var(--blue) 611px 100%);
  }
</style>
</head>
<body>
<div class="canvas">
  <section class="card">
    <header>
      <div class="header-band"></div>
      <h1 class="headline">Our purpose is clear, we get companies<br>and their founders, fit, funded, big and out</h1>
      <div class="brand-tab">
        <span class="brand-dot"></span>
        <span class="brand-name">Thornwell<br>Advisory</span>
      </div>
    </header>

    <div class="stage-spine"></div>

    <div class="stage" style="top:242px"><div class="stage-core">Get<br>Fit</div></div>
    <div class="stage" style="top:407px"><div class="stage-core">Get<br>Funded</div></div>
    <div class="stage" style="top:574px"><div class="stage-core">Get<br>Big</div></div>
    <div class="stage" style="top:740px"><div class="stage-core">Get<br>Out</div></div>

    <div class="stage-link" style="top:316px"></div>
    <div class="stage-link" style="top:482px"></div>
    <div class="stage-link" style="top:648px"></div>
    <div class="stage-link" style="top:814px"></div>

    <div class="goal" style="top:213px">Disciplined</div>
    <div class="element-row" style="top:292px">
      <div class="element">Vision</div>
      <div class="element">Strategy</div>
      <div class="element">Structure</div>
    </div>

    <div class="goal" style="top:378px">Access to Capital</div>
    <div class="element-row" style="top:458px">
      <div class="element">Product &amp; Services</div>
      <div class="element">Sales &amp; Marketing</div>
      <div class="element">System &amp; Processes</div>
    </div>

    <div class="goal" style="top:544px">Grow</div>
    <div class="element-row" style="top:624px">
      <div class="element">People</div>
      <div class="element">Culture</div>
      <div class="element">Finance</div>
    </div>

    <div class="goal" style="top:709px">Exit with Wealth</div>
    <div class="element-row" style="top:790px">
      <div class="element">M&amp;A</div>
      <div class="element">Performance<br>Monitoring</div>
      <div class="element">Risk<br>Management</div>
    </div>

    <div class="footer-bar"></div>
  </section>
</div>
</body>
</html>
```